Barrister Letterhead incorporating existing logo/design

Require new letterhead template to incorporate logo and information on 'Letter 2015' word document. Currently the information on the letterhead is very busy and would like a cleaner look.
Must look good in black and white, and colour when printed.

Target Market(s)

Professional

Industry/Entity Type

Legal

Requirements
Must have
• Clean professional look.

```html
<!DOCTYPE html>
<html lang="en">
<head>
<meta charset="utf-8">
<title>Harrow Chambers Letterhead</title>
<link rel="stylesheet" href="https://fonts.googleapis.com/css2?family=EB+Garamond:wght@400&family=Questrial&display=swap">
<style>
  :root {
    --backdrop: #d6d6d8;
    --paper: #ffffff;
    --navy: #1f2a4a;
    --ink: #1b1b1b;
    --muted: #6f7480;
    --footer-grey: #8d8d8f;
    --signature-tone: #dfe3f3;
  }
  * { margin: 0; padding: 0; box-sizing: border-box; }
  html, body { width: 1200px; height: 991px; overflow: hidden; }
  body { background: var(--backdrop); font-family: "Questrial", "Century Gothic", sans-serif; color: var(--ink); }
  .letterhead {
    position: absolute; left: 263px; top: 20px; width: 673px; height: 951px;
    background: var(--paper); box-shadow: 0 2px 6px rgba(0,0,0,0.18);
  }
  .brand { position: absolute; left: 55px; top: 50px; display: flex; align-items: flex-start; }
  .brand-mark { width: 43px; height: 37px; background: var(--navy); margin-right: 9px; }
  .brand-name {
    font-family: "EB Garamond", Georgia, serif; font-size: 23px; line-height: 21px;
    color: var(--navy); letter-spacing: 0.3px; padding-bottom: 3px;
    border-bottom: 1px solid #b9bccb;
  }
  .brand-tagline {
    font-family: "EB Garamond", Georgia, serif; font-size: 15px; line-height: 17px;
    color: var(--muted); letter-spacing: 2.1px; margin-top: 1px;
  }
  .address {
    position: absolute; right: 54px; top: 50px; text-align: right;
    font-size: 9.5px; line-height: 12px; color: #333; font-style: normal;
  }
  .letter-body { position: absolute; left: 55px; top: 282px; width: 565px; font-size: 10px; line-height: 12px; letter-spacing: -0.1px; }
  .salutation { font-weight: bold; margin-bottom: 12px; }
  .letter-body p { text-align: justify; margin-bottom: 12px; }
  .sign-off { position: absolute; left: 55px; top: 570px; font-size: 10px; line-height: 12px; }
  .signer { font-weight: bold; }
  .signature { position: absolute; left: 144px; top: 560px; width: 140px; height: 60px; background: var(--signature-tone); border-radius: 4px; }
  .footer { position: absolute; left: 52px; top: 905px; height: 18px; display: flex; font-size: 9px; line-height: 18px; }
  .footer-contact { width: 376px; background: var(--navy); color: #fff; padding: 0 8px 0 13px; white-space: nowrap; overflow: hidden; }
  .footer-contact b { font-weight: bold; }
  .footer-mark { width: 22px; height: 18px; background: var(--navy); margin-left: 4px; display: flex; align-items: center; justify-content: center; }
  .footer-mark span { width: 12px; height: 12px; border: 1px solid #fff; }
  .footer-web { width: 165px; background: var(--footer-grey); color: #fff; margin-left: 4px; text-align: right; padding-right: 9px; white-space: nowrap; }
</style>
</head>
<body>
  <main class="letterhead">
    <header>
      <div class="brand">
        <div class="brand-mark"></div>
        <div>
          <div class="brand-name">HARROW CHAMBERS</div>
          <div class="brand-tagline">Barristers and Mediators</div>
        </div>
      </div>
      <address class="address">Level 2, 24 Marlow Street<br>Kirwan QLD 4817</address>
    </header>

    <section class="letter-body">
      <div class="salutation">Dear sir,</div>
      <p>Communication is a very integral part of living creatures, animals and humans. Communication may be verbal or written. Written communication however is only applicable to human beings. Can you even imagine a world without communication? Verbal communication can be through telephones, webcams or in person. Written communication is through letters, emails and mobile phone messages.</p>
      <p>In today’s world of great inventions and technology, letters have somehow become redundant. It is the time for text messages or chats. But they still can communicate a lot more than all other modes of communication. Organizations and various government departments still bank on letters as a strong medium of communication. There is no comparison in costs of sending letters as compared to costs of mobile phone messages though – letters are far cheaper. Letters now commonly known as “hard copy documents” are considered more relevant and important than email copies of text messages as proof or evidence of some sort.</p>
      <p>Letters speak volumes about a person or an organization that writes it. So one must take utmost care ensuring that the language used in any letter is appropriate for the occasion for which it is being written. Since a letter is also a written proof or document, if there are certain things that should not form a part of it, then that too should be carefully handled.</p>
      <p>Writing a good letter is an art. But if for some reason someone is unable to write that perfect letter, these different types of letters provide a base for you to build on. Sample letters have been given for everyone to understand what all information needs to form a part of the letter type and then it can be customized.</p>
    </section>

    <div class="sign-off">Yours Sincerely,<br><span class="signer">Elena Varrow</span></div>
    <div class="signature" role="img" aria-label="Handwritten signature"></div>

    <footer class="footer">
      <div class="footer-contact">HARROW CHAMBERS · <b>T:</b> 07 4000 1182 · <b>F:</b> 07 4000 1190 · <b>E:</b> ev@harrowbar.asn.au</div>
      <div class="footer-mark"><span></span></div>
      <div class="footer-web">www.<b>harrowchambers.com</b>.au</div>
    </footer>
  </main>
</body>
</html>
```